Personal Development company in need for a fun website

KV7 effectively encourages personal growth and self-improvement by providing the positive tools which will motivate, enlighten and empower the client in a relaxed, friendly environment. Taking care of the ‘self’ is essential to being productive and valuable in all aspects of life, professionally and personally. We want it to be edgy and fun targeting professionals, youth and women entering the workforce.

We would need a homepage that would have a news and features, an online shop for some of our products, a schedule for our events and workshops, a calendar, an about us section and team. Other features that need to be added terms and conditions, privacy, link to social media on the bottom of the home page.

Please look at brain dock and the hall of dawns to understand our concept.

Target Market(s)

Young professionals, women that want to enter the workplace, individuals of all ages seeking personal development in all its forms.

Industry/Entity Type

It Company

Coding

Coded - Design and coding required

Number of Pages Required

5+ page

Font styles to use
Sans Serif

Requirements
Must have
• Must be clean and attractive.
Nice to have
• Graphic design work
Should not have
• Photographs, unless its the speaker of an event.

```html
<!DOCTYPE html>
<html lang="en">
<head>
<meta charset="utf-8">
<title>KV7 – Personal Development</title>
<link href="https://fonts.googleapis.com/css2?family=Montserrat:wght@400;500;600;700&family=Open+Sans:ital,wght@0,400;0,600;0,700;1,400&display=swap" rel="stylesheet">
<style>
:root{
  --dark:#333333;
  --darker:#262626;
  --topbar:#3a3a3a;
  --red:#c21f2f;
  --orange:#f05a28;
  --orange-soft:#f38a6a;
  --blue:#1b9be0;
  --grey-bg:#f3f3f3;
  --line:#dcdcdc;
  --text:#555555;
  --muted:#8a8a8a;
  --heading:#222222;
  --white:#ffffff;
}
*{box-sizing:border-box;margin:0;padding:0}
html,body{width:1200px;height:2317px;overflow:hidden}
body{font-family:"Open Sans",Arial,sans-serif;color:var(--text);background:var(--white);position:relative;font-size:11px}
.abs{position:absolute}
a{color:inherit;text-decoration:none}
h1,h2,h3,h4{font-family:"Montserrat",Arial,sans-serif;font-weight:600;color:var(--heading)}

/* top bar */
.topbar{top:0;left:0;width:1200px;height:25px;background:var(--topbar);color:#cfcfcf;font-size:10px}
.topbar .links{left:207px;top:6px;display:flex;gap:26px}
.topbar .contact{left:727px;top:6px}
.topbar .user{left:885px;top:6px}

/* header */
.header{top:25px;left:0;width:1200px;height:71px;background:var(--white);border-bottom:1px solid #e8e8e8}
.brand{left:207px;top:22px;display:flex;align-items:center;gap:8px}
.brand-mark{width:10px;height:10px;background:var(--heading)}
.brand-name{font-family:"Montserrat",sans-serif;font-weight:600;font-size:22px;color:var(--heading);letter-spacing:1px}
.nav{left:442px;top:33px;display:flex;font-family:"Montserrat",sans-serif;font-size:11px;color:#333}
.nav a{margin-right:27px}
.nav a.active{color:var(--orange)}
.nav .search{margin-left:-6px}
.cart{left:859px;top:31px;font-family:"Montserrat",sans-serif;font-weight:600;font-size:10px;color:#222;display:flex;align-items:center;gap:6px}
.bag{left:966px;top:24px}
.badge{left:978px;top:22px;width:12px;height:12px;border-radius:50%;background:#1a3a9e;color:#fff;font-size:8px;text-align:center;line-height:12px}

/* hero */
.hero{top:96px;left:0;width:1200px;height:318px;background:radial-gradient(ellipse at 35% 40%,#c9c9cf 0%,#8f8f98 55%,#6e6e78 100%)}
.hero-person{left:222px;top:18px;width:230px;height:300px;border-radius:110px 110px 0 0;background:linear-gradient(180deg,#a9a6a5,#7b7d86)}
.hero-title{left:677px;top:96px;font-family:"Montserrat",sans-serif;font-weight:500;font-size:21px;line-height:27px;color:#fff;letter-spacing:.5px}
.hero-sub{left:677px;top:159px;font-size:12px;color:#eee}
.hero-sub b{font-weight:700}
.btn{display:inline-block;font-family:"Montserrat",sans-serif;font-weight:600;font-size:8px;letter-spacing:.5px;text-transform:uppercase;color:#fff;text-align:center}
.hero-btns{left:677px;top:210px;display:flex;gap:10px}
.hero-btns .btn{width:85px;height:21px;line-height:21px}
.btn-dark{background:#3a3a3a}
.btn-red{background:var(--red)}
.hero-arrow{top:150px}

/* resources band */
.band{top:414px;left:0;width:1200px;height:83px;background:#f6f6f6}
.band-orange{top:0;left:0}
.band-count{left:207px;top:20px;font-family:"Montserrat",sans-serif;font-size:17px;color:#555}
.band-sub{left:207px;top:44px;font-family:"Montserrat",sans-serif;font-size:12px;color:var(--red);font-weight:500}
.band-input{left:723px;top:28px;width:232px;height:28px;background:#fff;color:#aaa;font-size:10px;padding:7px 9px}
.band-btn{left:955px;top:28px;width:35px;height:28px;background:var(--red)}

/* welcome */
.welcome-title{left:207px;top:577px;font-size:26px;font-weight:600}
.welcome-text{left:207px;top:621px;width:472px;font-size:9.5px;line-height:14px;color:#555}
.read-more{font-family:"Montserrat",sans-serif;font-size:9px;letter-spacing:.5px;color:var(--orange);display:flex;align-items:center;gap:4px}
.welcome-more{left:207px;top:696px}

/* products */
.products-band{top:752px;left:0;width:1200px;height:371px;background:var(--grey-bg)}
.section-title{font-size:16px;font-weight:600}
.products-title{left:207px;top:790px}
.pager{display:flex;gap:3px}
.pager span{width:16px;height:16px;border:1px solid #bbb;background:#fff;display:flex;align-items:center;justify-content:center}
.pager span.on{background:var(--orange);border-color:var(--orange)}
.products-pager{left:620px;top:788px}
.product{top:839px;width:139px}
.product .shot{height:142px;background:#fff;display:flex;align-items:center;justify-content:center}
.product .box{width:58px;height:90px;border-radius:3px}
.product.hover .shot{background:var(--orange-soft)}
.product .name{margin-top:12px;font-size:10px;line-height:14px;color:#444}
.price{margin-top:10px;font-family:"Montserrat",sans-serif;font-weight:600;font-size:19px;color:var(--red)}
.price sup{font-size:10px}
.product .btn{margin-top:8px;width:85px;height:21px;line-height:21px}

/* experts */
.experts-title{left:207px;top:1168px}
.experts-pager{left:617px;top:1166px}
.expert-photo{left:209px;top:1222px;width:114px;height:114px;border-radius:50%;background:linear-gradient(180deg,#dfe6ee,#8a97a8);border:3px solid #fff;box-shadow:0 0 0 1px #ddd}
.quote{left:343px;top:1233px;width:314px;font-size:9.5px;line-height:15px;font-style:italic;color:#555}
.expert-name{left:343px;top:1358px;font-family:"Montserrat",sans-serif;font-size:15px;color:#333}
.expert-role{left:343px;top:1377px;font-size:9px;color:#666}

/* call to action */
.cta{left:207px;top:1445px;width:451px;height:229px;background:var(--blue);box-shadow:4px 4px 0 #e3e3e3}
.cta h3{position:absolute;left:44px;top:36px;font-weight:400;font-size:19px;color:#fff}
.cta h4{position:absolute;left:44px;top:63px;font-weight:600;font-size:15px;color:#fff}
.cta p{position:absolute;left:44px;top:95px;width:360px;font-weight:600;font-size:12px;line-height:16px;color:#eaf6ff}
.cta .btn{position:absolute;left:44px;top:164px;width:113px;height:29px;line-height:29px;background:#3a3a3a;font-size:9px}

/* newsletter */
.sub-title{left:207px;top:1733px;font-size:16px}
.sub-text{left:207px;top:1779px;font-size:11px;color:#555}
.field{left:207px;width:249px;height:22px;border:1px solid #ddd;background:#fff;font-size:9px;color:#999;padding:4px 9px}
.sub-btn{left:207px;top:1889px;width:79px;height:22px;line-height:22px}
.sub-note{left:307px;top:1887px;font-size:9px;line-height:12px;color:#555}
.sub-note u{color:#333}

/* events */
.events-box{left:745px;top:640px;width:247px;height:580px;border:1px solid #ddd;background:#fff}
.events-disc{left:748px;top:540px}
.disc-text{left:768px;width:200px;text-align:center;color:#fff;font-family:"Montserrat",sans-serif}
.upcoming{left:768px;top:808px;width:200px;text-align:center;font-size:12px;line-height:16px}
.event{left:767px;width:205px;border-bottom:1px solid #e3e3e3}
.event .date{font-family:"Montserrat",sans-serif;font-size:17px;color:var(--orange)}
.event .desc{margin-top:6px;font-size:9.5px;line-height:14px;color:#555}
.event .desc.link{color:var(--red);text-decoration:underline}
.event .tag{margin-top:8px;font-size:9px;color:#999;display:flex;align-items:center;gap:4px}
.view-all{width:85px;height:22px;line-height:22px;background:#3a3a3a}

/* latest update */
.update-box{left:745px;top:1244px;width:247px;height:667px;border:1px solid #ddd;background:#fff}
.update-head{left:745px;top:1244px;width:247px;height:41px;background:var(--red);color:#fff;font-family:"Montserrat",sans-serif;font-size:16px;padding:10px 19px;font-weight:500}
.update-head b{font-weight:700}
.post{left:766px;width:205px}
.post .thumb{height:105px}
.post h4{margin-top:12px;font-family:"Open Sans",sans-serif;font-weight:400;font-size:11px;line-height:15px;color:#333}
.post .meta{margin-top:5px;font-size:8.5px;color:#999}
.post .rule{margin-top:8px;border-top:1px solid #e6e6e6}
.post p{margin-top:10px;font-size:9.5px;line-height:14px;color:#666}
.post .read-more{margin-top:12px;color:#333}

/* footer */
.footer{top:1954px;left:0;width:1200px;height:297px;background:var(--dark);color:#cfcfcf}
.f-col{top:40px}
.f-col h4{color:#fff;font-size:12px;font-weight:600;padding-bottom:12px;border-bottom:1px solid #666;margin-bottom:12px}
.f-links{list-style:none;font-size:10px;line-height:14px}
.f-links li::before{content:"• ";color:#aaa}
.f-links li.on{color:var(--orange)}
.f-social-title{margin-top:10px;color:#fff;font-weight:600;font-size:10px}
.socials{margin-top:8px;display:flex;gap:3px}
.socials span{width:23px;height:23px;background:#666;border:1px solid #888;color:#eee;font-size:8px;font-weight:700;display:flex;align-items:center;justify-content:center}
.socials span.on{background:var(--red);border-color:var(--red)}
.f-text{font-size:10px;line-height:14px;color:#cfcfcf}
.f-big{font-family:"Montserrat",sans-serif;font-size:17px;color:#fff;margin:10px 0 14px}
.f-btn{margin-top:12px;width:85px;height:22px;line-height:22px;border:1px solid #777;background:#444}
.f-bold{color:#fff;font-weight:600}

.bottom{top:2251px;left:0;width:1200px;height:66px;background:var(--darker);color:#bbb;font-size:10px}
.bottom .copy{left:207px;top:28px}
.cards{left:845px;top:21px;display:flex;gap:4px}
.cards span{width:34px;height:24px;background:#f2f2f2;border-radius:3px;color:#333;font-size:7.5px;font-weight:700;display:flex;align-items:center;justify-content:center}
</style>
</head>
<body>

<div class="abs topbar">
  <div class="abs links"><a href="#">Home</a><a href="#">About Us</a><a href="#">Contact Us</a></div>
  <div class="abs contact">Questions? Call &#9742; 555-010-274</div>
  <div class="abs user">User &#128274; Login / Register</div>
</div>

<header class="abs header">
  <div class="abs brand">
    <span class="brand-mark"></span>
    <span class="brand-name">KV7</span>
  </div>
  <nav class="abs nav">
    <a class="active" href="#">Products</a>
    <a href="#">Events &amp; Work Shops</a>
    <a href="#">Coching</a>
    <a href="#">Team</a>
    <a href="#">Blog</a>
    <svg class="search" width="12" height="12" viewBox="0 0 12 12"><circle cx="5" cy="5" r="3.6" fill="none" stroke="#222" stroke-width="1.6"/><line x1="7.6" y1="7.6" x2="11" y2="11" stroke="#222" stroke-width="1.8"/></svg>
  </nav>
  <div class="abs cart">
    <svg width="10" height="9" viewBox="0 0 10 9"><rect y="0" width="10" height="1.6" fill="#222"/><rect y="3.7" width="10" height="1.6" fill="#222"/><rect y="7.4" width="10" height="1.6" fill="#222"/></svg>
    Cart / $2000.00
  </div>
  <svg class="abs bag" width="20" height="20" viewBox="0 0 20 20"><path d="M3 7h14l-1 12H4z" fill="none" stroke="#222" stroke-width="1.6"/><path d="M7 7V5a3 3 0 0 1 6 0v2" fill="none" stroke="#222" stroke-width="1.6"/></svg>
  <div class="abs badge">0</div>
</header>

<section class="abs hero" role="img" aria-label="Grey studio backdrop with a smiling young professional in a grey suit working at a laptop">
  <div class="abs hero-person"></div>
  <svg class="abs hero-arrow" style="left:150px" width="16" height="14" viewBox="0 0 16 14"><path d="M15 7H2M7 1.5 1.5 7 7 12.5" fill="none" stroke="#222" stroke-width="1.8"/></svg>
  <svg class="abs hero-arrow" style="left:1036px" width="16" height="14" viewBox="0 0 16 14"><path d="M1 7h13M9 1.5 14.5 7 9 12.5" fill="none" stroke="#fff" stroke-width="1.8"/></svg>
  <h1 class="abs hero-title">Contribute, Participate,<br>Learn and Grow</h1>
  <p class="abs hero-sub">Join the and Get immediate access to <b>$499</b> worth<br>of Inspiring Products</p>
  <div class="abs hero-btns"><a class="btn btn-dark" href="#">Shop Now</a><a class="btn btn-red" href="#">Join Now</a></div>
</section>

<section class="abs band">
  <svg class="abs band-orange" width="1200" height="83" viewBox="0 0 1200 83"><polygon points="680,0 1200,0 1200,83 700,83 716,42" fill="#f05a28"/></svg>
  <div class="abs band-count">453,690 Self Improvement Resources</div>
  <div class="abs band-sub">Find the Right One for You</div>
  <div class="abs band-input">Type here ....</div>
  <div class="abs band-btn"><svg width="35" height="28" viewBox="0 0 35 28"><circle cx="16.5" cy="13" r="3.6" fill="none" stroke="#fff" stroke-width="1.5"/><line x1="19" y1="15.5" x2="22" y2="18.5" stroke="#fff" stroke-width="1.6"/></svg></div>
</section>

<h2 class="abs welcome-title">Welcome to KV7</h2>
<p class="abs welcome-text">Lorem Ipsum is simply dummy text of the printing and typesetting industry. Lorem Ipsum has been theindustry's standard dummy text ever since the 1500s, when an unknown printer took a galley of type and scrambled it to make a type specimen book. It has survived not only five centuries, but also the leap into electronic typesetting, ...</p>
<a class="abs read-more welcome-more" href="#"><svg width="8" height="8" viewBox="0 0 8 8"><circle cx="4" cy="4" r="3.3" fill="none" stroke="currentColor" stroke-width="1.2"/></svg>READ MORE</a>

<section class="abs products-band"></section>
<h2 class="abs section-title products-title">Self Help Products</h2>
<div class="abs pager products-pager">
  <span><svg width="6" height="8" viewBox="0 0 6 8"><path d="M5 1 2 4l3 3" fill="none" stroke="#666" stroke-width="1.3"/></svg></span>
  <span class="on"><svg width="6" height="8" viewBox="0 0 6 8"><path d="M1 1l3 3-3 3" fill="none" stroke="#fff" stroke-width="1.3"/></svg></span>
</div>

<div class="abs product" style="left:207px">
  <div class="shot"><div class="box" role="img" aria-label="Blue audio program box" style="background:#2a74d0"></div></div>
  <div class="name">Daily Steps to Calm Focus<br>MP3 Version</div>
  <div class="price">$49<sup>.95</sup></div>
  <a class="btn btn-red" href="#">Add to cart</a>
</div>
<div class="abs product hover" style="left:363px">
  <div class="shot"><svg width="30" height="30" viewBox="0 0 30 30"><path d="M15 3v24M3 15h24" stroke="#fff" stroke-width="1.6"/></svg></div>
  <div class="name">Finding Your Own<br>Direction MP3 Version</div>
  <div class="price">$49<sup>.95</sup></div>
  <a class="btn btn-dark" href="#">Add to cart</a>
</div>
<div class="abs product" style="left:518px">
  <div class="shot"><div class="box" role="img" aria-label="Teal audio program box" style="background:#22b8c2"></div></div>
  <div class="name">Building Steady Confidence<br>MP3 Version</div>
  <div class="price">$49<sup>.95</sup></div>
  <a class="btn btn-dark" href="#">Add to cart</a>
</div>

<h2 class="abs section-title experts-title">What Experts&nbsp; Are Saying?</h2>
<div class="abs pager experts-pager">
  <span><svg width="6" height="8" viewBox="0 0 6 8"><path d="M5 1 2 4l3 3" fill="none" stroke="#666" stroke-width="1.3"/></svg></span>
  <span><svg width="6" height="8" viewBox="0 0 6 8"><path d="M1 1l3 3-3 3" fill="none" stroke="#666" stroke-width="1.3"/></svg></span>
</div>
<div class="abs expert-photo" role="img" aria-label="Portrait of the quoted executive producer"></div>
<p class="abs quote">" Lorem Ipsum is simply dummy text of the printing and typesetting industry. Lorem Ipsum has been the industry's standard dummy text ever since the 1500s, when an unknown printer took a galley of type and scrambled it to make a type specimen book. It has survived not only five centuries, but also the leap into electronic. "</p>
<div class="abs expert-name">Dale Harwood,</div>
<div class="abs expert-role">Executive Producer, Northbound</div>

<section class="abs cta">
  <h3>Are you ready to transform your life?</h3>
  <h4>Let me be there to guide you</h4>
  <p>Quisque sit amet est et sapien ullamcorper pharetra. Vestibulum erat wisi, condimentum sed, commodo vitae, ornare sit amet, wisi. Aenean fermentum.</p>
  <a class="btn" href="#">Sign up now</a>
</section>

<h2 class="abs sub-title">Subscribe Newsletter</h2>
<p class="abs sub-text">Sign up now to receive a daily news, updates and more.</p>
<div class="abs field" style="top:1812px">Name</div>
<div class="abs field" style="top:1846px">Email</div>
<a class="abs btn btn-dark sub-btn" href="#">Subscribe</a>
<p class="abs sub-note">You may unsubscribe at anytime.<br>Read our <u>Privacy Policy</u>.</p>

<div class="abs events-box"></div>
<svg class="abs events-disc" width="240" height="260" viewBox="0 0 240 260">
  <circle cx="120" cy="122" r="116" fill="#e9e9e9"/>
  <polygon points="98,225 142,225 120,256" fill="#e9e9e9"/>
  <circle cx="120" cy="122" r="111" fill="#f05a28"/>
  <polygon points="100,225 140,225 120,250" fill="#f05a28"/>
  <path d="M14.7 87A111 111 0 0 1 225.3 87Z" fill="#c21f2f"/>
</svg>
<div class="abs disc-text" style="top:566px;font-size:16px;line-height:17px">LATEST</div>
<div class="abs disc-text" style="top:585px;font-size:12px;line-height:16px;font-weight:600">Events &amp; Work<br>Shops</div>
<div class="abs disc-text" style="top:652px;font-size:17px;color:#3a1a10">03 / Feb, 2016</div>
<div class="abs disc-text" style="top:677px;font-size:10px;line-height:13px;font-weight:600;color:#3a1a10;font-family:'Open Sans',sans-serif">Webinar on Forecasting for<br>Profit: The Basics</div>
<a class="abs btn view-all" style="left:828px;top:717px;width:80px;height:20px;line-height:20px" href="#">More detail</a>

<h3 class="abs upcoming">Upcoming<br>Events &amp; Work Shops</h3>

<div class="abs event" style="top:864px;height:92px">
  <div class="date">07 / Oct, 2016</div>
  <div class="desc">Tools and Techniques for Team Safety Training - By Ridgeway Standards Inc.</div>
  <div class="tag">&#9679; Work Shops</div>
</div>
<div class="abs event" style="top:971px;height:94px">
  <div class="date">07 / Apr, 2016</div>
  <div class="desc link">Tools and Techniques for Team Safety Training - By Ridgeway Standards Inc.</div>
  <div class="tag">&#9679; Events</div>
</div>
<div class="abs event" style="top:1081px;border-bottom:none">
  <div class="date">07 / Jun, 2016</div>
  <div class="desc">Tools and Techniques for Team Safety Training - By Ridgeway Standards Inc.</div>
  <div class="tag">&#9679; Work Shops</div>
</div>
<a class="abs btn view-all" style="left:766px;top:1179px" href="#">View all</a>

<div class="abs update-box"></div>
<div class="abs update-head">Latest <b>Update</b></div>
<article class="abs post" style="top:1307px">
  <div class="thumb" role="img" aria-label="Photographer kneeling on a mountain ridge at sunset" style="background:linear-gradient(180deg,#d9b48a,#8a8e98 60%,#4b5058)"></div>
  <h4>Books Coming to the Big Screen in 2016</h4>
  <div class="meta">- By Ivo Castell&nbsp; / &nbsp;6 Jan, 2016</div>
  <div class="rule"></div>
  <p>It's exhilarating (and a little scary) when our favorite books are made into motion pictures. The idea of seeing ...</p>
  <a class="read-more" href="#"><svg width="8" height="8" viewBox="0 0 8 8"><circle cx="4" cy="4" r="3.3" fill="none" stroke="currentColor" stroke-width="1.2"/></svg>READ MORE</a>
</article>
<article class="abs post" style="top:1587px">
  <div class="thumb" role="img" aria-label="Stacked stones on a mountain top under a blue sky" style="background:linear-gradient(180deg,#6f94c4,#a8b6c6 55%,#8c7c62)"></div>
  <h4>10 2016 YA Books with Utterly Irresistible Concepts</h4>
  <div class="meta">- By Nora Wendt&nbsp; / &nbsp;11 Feb, 2016</div>
  <div class="rule"></div>
  <p>It's exhilarating (and a little scary) when our favorite books are made into motion pictures. The idea of seeing ...</p>
  <a class="read-more" href="#"><svg width="8" height="8" viewBox="0 0 8 8"><circle cx="4" cy="4" r="3.3" fill="none" stroke="currentColor" stroke-width="1.2"/></svg>READ MORE</a>
</article>
<a class="abs btn view-all" style="left:766px;top:1866px" href="#">View all</a>

<footer class="abs footer">
  <div class="abs f-col" style="left:207px;width:180px">
    <h4>Quick Link</h4>
    <ul class="f-links">
      <li>Home</li><li class="on">About Us</li><li>Products</li><li>Events &amp; Work Shops</li><li>Coching</li><li>Team</li><li>Blog</li><li>Contact Us</li>
    </ul>
    <div class="f-social-title">Conect with Social:</div>
    <div class="socials">
      <span aria-label="Friendloop">Fl</span><span class="on" aria-label="Circlet">Ci</span><span aria-label="Chirpline">Ch</span><span aria-label="Snapframe">Sf</span><span aria-label="Reelbox">Rb</span><span aria-label="Workweave">Ww</span>
    </div>
  </div>
  <div class="abs f-col" style="left:419px;width:244px">
    <h4>Customer Service &amp; Sales</h4>
    <p class="f-text">For inquiries, or to place an order over the phone, call our staff at:</p>
    <div class="f-big">1-800-555-0142</div>
    <p class="f-text"><span class="f-bold">Mon to Sat</span><br>8:30am to 5pm Central Time We take pride in our fast and courteous customer service.</p>
    <p class="f-text" style="margin-top:12px">Click here for email support</p>
    <a class="btn f-btn" href="#">Contact us</a>
  </div>
  <div class="abs f-col" style="left:725px;width:267px">
    <h4>30-Day Money-Back Guarantee</h4>
    <p class="f-text">At Larkspur - Bennett, your satisfaction is our #1 priority - and it's</p>
    <div class="f-big">100% Guarantee</div>
    <p class="f-text">Growth Circle Members receive a 60 days return exchange policy on CD or DVD programs* purchase with an active membership.*Due to the nature of Digital purchases, Digital Downloads such as ...</p>
    <a class="read-more" style="margin-top:16px;color:#ddd" href="#"><svg width="8" height="8" viewBox="0 0 8 8"><circle cx="4" cy="4" r="3.3" fill="none" stroke="currentColor" stroke-width="1.2"/></svg>READ MORE</a>
  </div>
</footer>

<div class="abs bottom">
  <div class="abs copy">© 2016 KV7. All rights reserved. Terms &amp; Conditions&nbsp; I&nbsp; Privacy &amp; Policy</div>
  <div class="abs cards"><span>Paylo</span><span>Cardix</span><span>Tendro</span><span>Walletly</span></div>
</div>

</body>
</html>
```